Home Inspection Postcard Design

Home inspection. Attached is my old postcard. I would like the card to have the same verbage on it - front and back. but I would like the house graphic and the colors to be blues. The only changes to the information is the website address is www.brightoakhps.com. THe PO Box is now 381 rather than 647, and I wanted to add my email address which is brightoakhps@quillmail.net. I would like to keep the $25 off box but add "or a 10% military discount, which ever is greater" or something like that .If you could mock something up for me I would really appreciate it. I would also like a glossy finish on the cards

Home Inspection

```html
<!DOCTYPE html>
<html lang="en">
<head>
<meta charset="utf-8">
<title>Brightoak Home Inspection Postcard</title>
<link href="https://fonts.googleapis.com/css2?family=Oswald:wght@600;700&family=Open+Sans:wght@400;600&family=Lato:wght@400;700&display=swap" rel="stylesheet">
<style>
  :root{
    --blue:#1a73e8;
    --blue-deep:#0b5bd3;
    --blue-light:#3d8ff0;
    --orange:#f9a51a;
    --orange-light:#ffc94a;
    --dark:#2b2b2b;
    --ink:#222;
    --white:#fff;
    --stage:#e8e6e2;
    --photo-a:#c9b877;
    --photo-b:#7e8a5a;
  }
  *{box-sizing:border-box;margin:0;padding:0}
  html,body{width:907px;height:1200px;overflow:hidden}
  body{background:var(--stage);position:relative;font-family:"Open Sans",sans-serif}

  .card{position:absolute;background:var(--white);overflow:hidden;box-shadow:0 4px 14px rgba(0,0,0,.25)}
  .card-front{left:125px;top:58px;width:660px;height:512px}
  .card-back{left:125px;top:628px;width:658px;height:512px}
  .card svg.art{position:absolute;left:0;top:0}

  .brand{position:absolute;text-align:center;font-family:"Lato",sans-serif;color:var(--ink)}
  .brand-name{display:flex;align-items:center;justify-content:center;gap:6px;font-size:18px;font-weight:700;color:var(--ink)}
  .brand-dot{width:13px;height:13px;border-radius:50%;background:var(--blue-deep);display:inline-block}
  .brand-line{font-size:9.5px;line-height:13px}
  .front-brand{left:200px;top:24px;width:170px}
  .back-brand{left:318px;top:28px;width:150px}
  .back-brand .brand-line{font-size:9px}

  .front-title{position:absolute;right:20px;top:60px;text-align:right}
  .front-title h1{font-family:"Oswald",sans-serif;font-weight:700;font-size:44px;line-height:48px;color:var(--white)}
  .front-title h2{font-family:"Open Sans",sans-serif;font-weight:600;font-size:31px;line-height:40px;color:var(--orange)}

  .front-copy{position:absolute;left:362px;top:164px;width:280px;color:var(--white);font-size:12.2px;line-height:15.6px;text-align:justify;text-align-last:right}
  .front-copy p{margin-bottom:10px}
  .front-copy p:first-child{padding-left:4px}
  .front-copy p:nth-child(2){padding-left:30px}

  .offer{position:absolute;left:172px;top:342px;width:156px;height:156px;border-radius:50%;background:var(--orange);border:5px solid var(--white);box-shadow:0 0 0 3px var(--dark);text-align:center;color:var(--ink)}
  .offer-amount{font-family:"Oswald",sans-serif;font-weight:700;font-size:32px;line-height:36px;color:var(--white);margin-top:14px}
  .offer-label{font-size:21px;line-height:24px}
  .offer-note{font-size:12px;line-height:16px}
  .offer-extra{font-size:9.5px;line-height:12px;margin-top:2px;padding:0 14px}

  .contact-front{position:absolute;left:343px;top:438px;font-family:"Lato",sans-serif;color:var(--ink)}
  .contact-front h3{font-size:15px;font-weight:700;line-height:18px}
  .contact-row{display:flex;gap:22px;margin-top:6px;font-size:14px;line-height:18px;align-items:center}
  .contact-row span{display:flex;align-items:center;gap:6px}
  .contact-front .contact-mail{font-size:13px;line-height:18px;margin-top:2px}

  .back-title{position:absolute;left:19px;top:20px}
  .back-title h1{font-family:"Oswald",sans-serif;font-weight:700;font-size:38px;line-height:46px;color:var(--white)}
  .back-title h2{font-family:"Open Sans",sans-serif;font-weight:400;font-size:35px;line-height:42px;color:var(--orange)}

  .back-copy{position:absolute;left:19px;top:120px;width:370px;color:var(--white);font-family:"Lato",sans-serif;font-size:14px;line-height:17.8px;text-align:justify}
  .back-copy .curve-wrap{float:right;width:70px;height:300px;shape-outside:polygon(7px 0,46px 130px,54px 210px,50px 300px,70px 300px,70px 0)}

  .contact-back{position:absolute;left:19px;top:430px;font-family:"Lato",sans-serif;color:var(--ink)}
  .contact-back h3{font-size:15px;font-weight:700;line-height:18px;margin-bottom:3px}
  .contact-back p{display:flex;align-items:center;gap:10px;font-size:14px;line-height:19px}

  .stamp{position:absolute;left:560px;top:58px;width:72px;height:88px;border:1px solid #555}
  .address-line{position:absolute;left:437px;width:202px;height:1px;background:#555}
  .line-1{top:261px}
  .line-2{top:301px}
  .line-3{top:343px}
</style>
</head>
<body>

<section class="card card-front" aria-label="Postcard front">
  <svg class="art" width="660" height="512" viewBox="0 0 660 512">
    <defs>
      <linearGradient id="frontBlue" x1="0" y1="0" x2="1" y2="1">
        <stop offset="0" stop-color="#3d8ff0"/>
        <stop offset="1" stop-color="#0b5bd3"/>
      </linearGradient>
      <linearGradient id="housePhoto" x1="0" y1="0" x2="0" y2="1">
        <stop offset="0" stop-color="#dfe7ee"/>
        <stop offset=".35" stop-color="#c9b877"/>
        <stop offset="1" stop-color="#7e8a5a"/>
      </linearGradient>
    </defs>
    <rect x="300" y="0" width="360" height="432" fill="url(#frontBlue)"/>
    <polygon points="120,0 425,0 285,135 270,140 250,135" fill="#fff"/>
    <polyline points="250,135 270,140 285,135 425,0" fill="none" stroke="#f9a51a" stroke-width="3"/>
    <polygon points="0,0 130,0 0,130" fill="#2b2b2b"/>
    <polygon points="375,232 385,262 330,512 300,512" fill="#2b2b2b"/>
    <polygon role="img" aria-label="Photo of a two-storey house with white trim and a front garden" points="0,150 140,10 270,140 370,240 378,262 322,512 0,512" fill="url(#housePhoto)"/>
  </svg>

  <div class="brand front-brand">
    <div class="brand-name"><span class="brand-dot"></span>Brightoak</div>
    <div class="brand-line">Home Inspection Services LLC</div>
    <div class="brand-line">Licensed, Certified &amp; Insured</div>
  </div>

  <div class="front-title">
    <h1>Confidence In</h1>
    <h2>Home Buying</h2>
  </div>

  <div class="front-copy">
    <p>Enjoy the comfort or peace-of-rnrnd before buying your new home. Our trained professionals inspect the property and immediately present you with a detailed, yet clear report.They will answer any quesnons you may have.</p>
    <p>Join our experienced inspectors in their tour of the property. They will acquaint you with its strengths and weaknesses. You will feel confindent in their judgernen and thoroughness, any Realtors, sellers, home buyers, mortgage companies and relocation companies have used our comprehensive report and services to theirsatisfartion.</p>
  </div>

  <div class="offer">
    <div class="offer-amount">$25 off</div>
    <div class="offer-label">Services</div>
    <div class="offer-note">with this post card</div>
    <div class="offer-extra">or a 10% military discount, whichever is greater</div>
  </div>

  <div class="contact-front">
    <h3>To schedure your appointment Contact Us</h3>
    <div class="contact-row">
      <span>www.brightoakhps.com
        <svg width="11" height="11" viewBox="0 0 12 12"><circle cx="6" cy="6" r="5" fill="none" stroke="#f9a51a" stroke-width="1.5"/><path d="M1 6h10M6 1c-3 3-3 7 0 10M6 1c3 3 3 7 0 10" stroke="#f9a51a" fill="none"/></svg>
      </span>
      <span>912-555-0148
        <svg width="12" height="12" viewBox="0 0 12 12"><path d="M2 1l3 1-1 2 4 4 2-1 1 3-2 1C5 11 1 7 1 3z" fill="#f9a51a"/></svg>
      </span>
    </div>
    <div class="contact-mail">brightoakhps@quillmail.net</div>
  </div>
</section>

<section class="card card-back" aria-label="Postcard back">
  <svg class="art" width="658" height="512" viewBox="0 0 658 512">
    <defs>
      <linearGradient id="backBlue" x1="0" y1="0" x2="1" y2="1">
        <stop offset="0" stop-color="#0b5bd3"/>
        <stop offset="1" stop-color="#3d8ff0"/>
      </linearGradient>
      <linearGradient id="backOrange" x1="0" y1="0" x2="1" y2="0">
        <stop offset="0" stop-color="#f9a51a"/>
        <stop offset="1" stop-color="#ffc94a"/>
      </linearGradient>
    </defs>
    <path d="M0,0 H305 L380,250 Q392,290 388,330 L384,400 Q378,470 268,512 H0 Z" fill="#2b2b2b"/>
    <path d="M0,0 H298 L373,250 Q385,290 381,330 L377,400 Q371,465 262,512 H0 Z" fill="url(#backBlue)"/>
    <path d="M0,424 H376 Q366,478 262,512 H0 Z" fill="url(#backOrange)"/>
  </svg>

  <div class="back-title">
    <h1>Why Do I need</h1>
    <h2>An Inspection?</h2>
  </div>

  <div class="back-copy">
    <span class="curve-wrap"></span>
    The purchase of a home or commercial building is one of the largest single investments you will ever make. You should H know what to expect - in terms of needed and possible repairs and maintenance. A fresh coat of paint could be hiding serious problems. Stains on the ceiling may indicate a chronic roof leak or may be simply the result of a single incident. The inspector reviews these and other clues, then presents a professional opinion as to the condition of the property to help you avoid unpleasant surprises afterward. Of course, an inspection may also point out the positive aspects of a building, as well as the type of maintenance needed to keep it in proper shape. After the inspection, you will have a much clearer understanding of the property, and be able to make your purchasing decision confidently.
  </div>

  <div class="contact-back">
    <h3>To schedure your appointment Contact Us</h3>
    <p><svg width="12" height="12" viewBox="0 0 12 12"><path d="M2 1l3 1-1 2 4 4 2-1 1 3-2 1C5 11 1 7 1 3z" fill="#222"/></svg>912-555-0148</p>
    <p><svg width="12" height="12" viewBox="0 0 12 12"><circle cx="6" cy="6" r="5" fill="#222"/><path d="M1 6h10M6 1c-3 3-3 7 0 10M6 1c3 3 3 7 0 10" stroke="#fff" fill="none" stroke-width=".8"/></svg>www.brightoakhps.com</p>
    <p><svg width="12" height="12" viewBox="0 0 12 12"><rect x="1" y="2.5" width="10" height="7" fill="#222"/><path d="M1 3l5 4 5-4" stroke="#fff" fill="none" stroke-width=".8"/></svg>brightoakhps@quillmail.net</p>
  </div>

  <div class="brand back-brand">
    <div class="brand-name"><span class="brand-dot"></span>Brightoak</div>
    <div class="brand-line">Home Inspection Services LLC</div>
    <div class="brand-line">Licensed, Certified &amp; Insured</div>
  </div>

  <div class="stamp"></div>
  <div class="address-line line-1"></div>
  <div class="address-line line-2"></div>
  <div class="address-line line-3"></div>
</section>

</body>
</html>
```